32 x 24 Swinging Real Estate Yard Sign

We are looking to design a new sign for our business to focus on the remodeling of homes to sell. We are looking to have a yard sign that gets peoples attention and is informational. The headline will be "The Secret to Top Dollar? Remodel First.". We remodel homes for sellers with no up front cost, as they simply pay at closing. This link has more info, https://brightkeelhomes.com/Remodel
The message we want to convey to those seeing the sign is we are a one stop shop, who can renovate your home and sell it for no stress. We are licensed real estate agents and licensed contractors.
Both of these license numbers and info need to be on the design:
CADRE #02741968
Contractors License #2758314
Email: info@brightkeelhomes.com
Phone: (408)514-7290
I'll attach a sample sign we have for our agents normally as well as all brand art work.
• Pantone Colors
o #172A41
Dark blue
o #4381B1
Medium blue
o #6FA6CC
Light blue
Target Market(s)
Residential Real Estate Sellers
Industry/Entity Type
Real Estate
Colors
Designer to choose colors to be used in the design.

```html
<!DOCTYPE html>
<html lang="en">
<head>
<meta charset="utf-8">
<title>Brightkeel Homes – Remodel First Yard Sign</title>
<link href="https://fonts.googleapis.com/css2?family=Bebas+Neue&family=Montserrat:wght@500;600;800&display=swap" rel="stylesheet">
<style>
  :root {
    --dark-blue: #172A41;
    --medium-blue: #4381B1;
    --light-blue: #6FA6CC;
    --white: #FFFFFF;
    --backdrop: #E9ECEF;
  }
  * { margin: 0; padding: 0; box-sizing: border-box; }
  html, body {
    width: 1200px; height: 1200px; overflow: hidden;
    background: var(--backdrop);
  }
  .yard-sign {
    position: absolute; left: 180px; top: 40px;
    width: 840px; height: 1120px;
    display: flex; flex-direction: column;
    box-shadow: 0 10px 30px rgba(23, 42, 65, 0.25);
  }
  .sign-header {
    height: 400px; background: var(--dark-blue);
    position: relative;
    display: flex; flex-direction: column; align-items: center; justify-content: center;
  }
  .license {
    position: absolute; top: 26px;
    font-family: 'Bebas Neue', sans-serif; font-size: 30px; letter-spacing: 0.5px;
    color: var(--white);
  }
  .license--realtor { left: 34px; }
  .license--contractor { right: 24px; }
  .brand-dot {
    width: 90px; height: 90px; border-radius: 50%;
    background: var(--medium-blue); margin-bottom: 34px; margin-top: 40px;
  }
  .brand-name {
    font-family: 'Montserrat', sans-serif; font-weight: 600;
    font-size: 64px; letter-spacing: 3px; color: var(--white);
  }
  .sign-headline {
    height: 460px; background: var(--medium-blue);
    display: flex; flex-direction: column; align-items: center; justify-content: center;
    font-family: 'Bebas Neue', sans-serif; line-height: 0.93; text-align: center;
  }
  .headline-question {
    font-size: 150px; color: var(--white);
    text-shadow: 4px 4px 0 var(--dark-blue);
  }
  .headline-answer {
    font-size: 158px; color: var(--dark-blue);
  }
  .sign-contact {
    height: 260px; background: var(--dark-blue);
    display: flex; flex-direction: column; align-items: center; justify-content: center;
    font-family: 'Montserrat', sans-serif;
  }
  .contact-phone {
    font-weight: 800; font-size: 80px; color: var(--white); letter-spacing: 1px;
  }
  .contact-email {
    font-weight: 600; font-size: 38px; color: var(--medium-blue);
    letter-spacing: 2px; margin-top: 10px;
  }
</style>
</head>
<body>
  <main class="yard-sign">
    <header class="sign-header">
      <span class="license license--realtor">CADRE #02741968</span>
      <span class="license license--contractor">CONTRACTORS LICENSE #2758314</span>
      <div class="brand-dot"></div>
      <h1 class="brand-name">BRIGHTKEEL HOMES</h1>
    </header>
    <section class="sign-headline">
      <p class="headline-question">THE SECRET TO<br>TOP DOLLAR?</p>
      <p class="headline-answer">REMODEL FIRST</p>
    </section>
    <footer class="sign-contact">
      <p class="contact-phone">(408) 514-7290</p>
      <p class="contact-email">INFO@BRIGHTKEELHOMES.COM</p>
    </footer>
  </main>
</body>
</html>
```